Brochure for Veterinary Acupuncture and Physical Therapy
Willow Creek Pet Clinic
Putting the heart into healing
I am a veterinarian. My business is to travel from between existing veterinary practices to do acupucture and physical therapy with dogs and cats. This brochure will be something for the veterinary clinic to give their client about this service.
Animals
Veterinary pet owners
3 fold brochure
Photos and logo. Text will be coming in a separate upload. I'm not sure how much text is appropriate, so for now, can you put empty text boxes in designs so I can see how it might lay out? One section should be about me (picture of me with the dog), one section about acupuncture and one about physical therapy. Then another text box about how to schedule an appointment.
Me
Physical therapy picture
website: willowcreekpetclinic.net
email: willowcreekvet@postbloom.net
Also needs a facebook symbol
My business card, if that helps
Conditions treated -- depending on space I can shorten the physical therapy information
Overview
This is about me
Scheduling
New "training"
New mission

```html
<!DOCTYPE html>
<html lang="en">
<head>
<meta charset="utf-8">
<title>Willow Creek Pet Clinic – Trifold Brochure</title>
<link rel="stylesheet" href="https://fonts.googleapis.com/css2?family=Open+Sans:wght@400;600;700;800&display=swap">
<style>
  :root {
    --blue: #2c4f9e;
    --blue-deep: #223f82;
    --green: #5cb13c;
    --green-light: #8fd06a;
    --ink: #3a3a3a;
    --paper: #ffffff;
    --stage: #e8e4de;
    --photo-warm: #b89a78;
    --photo-cool: #8aa0b8;
  }
  * { box-sizing: border-box; margin: 0; padding: 0; }
  html, body { width: 1200px; height: 562px; overflow: hidden; }
  body {
    background: var(--stage);
    font-family: "Open Sans", Arial, sans-serif;
    color: var(--ink);
    position: relative;
  }
  .sheet {
    position: absolute;
    top: 41px;
    height: 480px;
    display: flex;
    box-shadow: 0 3px 10px rgba(0,0,0,.25);
  }
  .sheet--outside { left: 19px; width: 471px; background: var(--paper); }
  .sheet--inside { left: 545px; width: 633px; background: var(--blue); }
  .panel { position: relative; height: 100%; overflow: hidden; }
  .sheet--outside .panel { width: 157px; }
  .sheet--outside .panel + .panel { border-left: 1px solid #e4e4e4; }
  .sheet--inside .panel { width: 211px; }

  .photo { display: block; width: 100%; }
  .photo--warm { background: linear-gradient(160deg, #d9c3a2, var(--photo-warm) 60%, #7d6448); }
  .photo--cool { background: linear-gradient(160deg, #b9c7d6, var(--photo-cool) 55%, #5f7386); }
  .photo--grass { background: linear-gradient(180deg, #c9d7e4, #9fbf84 65%, #6f9a55); }
  .photo--bed { background: linear-gradient(170deg, #6b5440, #3f3228 55%, #5a79b8); }

  .body-copy { font-size: 6.3px; line-height: 1.45; margin-bottom: 5px; }

  /* About */
  .about .photo { height: 212px; }
  .about .content { padding: 10px 10px; }
  .about h2 { font-size: 7.5px; font-weight: 800; text-transform: uppercase; margin-bottom: 5px; color: var(--ink); }

  /* Scheduling */
  .schedule .photo { height: 104px; }
  .schedule .band {
    background: var(--blue); color: #fff; font-size: 8px; font-weight: 700;
    padding: 5px 9px; margin: 8px 0 8px;
  }
  .schedule .content { padding: 0 9px; }
  .schedule .note { color: var(--green); font-size: 7px; font-weight: 700; line-height: 1.35; margin: 6px 0 0; }
  .contact-list { list-style: none; position: absolute; left: 9px; bottom: 18px; }
  .contact-list li { display: flex; align-items: center; gap: 5px; font-size: 6.3px; color: var(--blue); margin-top: 4px; }
  .contact-list svg { width: 8px; height: 8px; flex: none; }

  /* Cover */
  .brand { display: flex; align-items: center; gap: 6px; }
  .brand__mark { width: 12px; height: 12px; border-radius: 50%; background: var(--green); flex: none; }
  .brand__name { font-weight: 700; color: var(--blue); font-size: 12px; line-height: 1.05; }
  .cover .brand-block { padding: 22px 12px 0; height: 96px; }
  .tagline { font-size: 5.6px; color: var(--green); margin-top: 5px; text-transform: uppercase; letter-spacing: .3px; }
  .rule { height: 3px; background: var(--green); margin-top: 8px; }
  .rule--blue { background: var(--blue); height: 2px; margin-top: 2px; }
  .cover .photo { height: 266px; }
  .cover .web { text-align: center; font-weight: 700; font-size: 9.5px; color: var(--blue); padding-top: 48px; }

  /* Inside */
  .inside-top { height: 7px; background: var(--green); }
  .overview .brand-block { padding: 14px 12px 12px; }
  .overview .brand__name { color: #fff; }
  .overview .brand__mark { background: var(--green-light); }
  .overview .tagline { color: var(--green-light); }
  .overview .body-copy { color: #fff; padding: 4px 12px 0; font-size: 6.5px; }
  .overview .photo { position: absolute; left: 0; bottom: 0; height: 178px; }

  .conditions .photo { height: 128px; }
  .conditions .band {
    background: var(--green); color: #fff; font-weight: 700; font-size: 9px;
    padding: 7px 10px;
  }
  .cond-list { list-style: none; columns: 2; column-gap: 8px; padding: 10px 12px; }
  .cond-list li { color: #fff; font-size: 6.4px; line-height: 1.9; break-inside: avoid; }
  .cond-list li::before { content: "•"; color: var(--green-light); margin-right: 3px; }

  .therapy { padding: 14px 12px 0; }
  .therapy h2 { color: #fff; font-size: 8.5px; font-weight: 700; line-height: 1.3; margin-bottom: 8px; }
  .therapy-list { list-style: none; }
  .therapy-list li { color: #fff; font-size: 6.3px; line-height: 1.45; margin-bottom: 6px; }
  .therapy-list b { color: var(--green-light); font-weight: 700; }

  .slogan-bar {
    position: absolute; left: 211px; right: 0; bottom: 0; height: 30px;
    background: var(--green); color: #fff; font-size: 11px; font-weight: 600;
    letter-spacing: .5px; display: flex; align-items: center; justify-content: center;
  }
</style>
</head>
<body>

<section class="sheet sheet--outside">
  <article class="panel about">
    <div class="photo photo--warm" role="img" aria-label="Photo of the veterinarian with her dog"></div>
    <div class="content">
      <h2>Meet Dr. Nora Hale</h2>
      <p class="body-copy">Dr. Hale has practiced veterinary medicine for over fifteen years and now brings acupuncture and physical therapy directly to partner clinics across the region.</p>
      <p class="body-copy">She trained in integrative care and canine rehabilitation, and works alongside your regular veterinarian to build a plan that fits each pet, whether recovering from surgery or managing a chronic condition.</p>
      <p class="body-copy">Her goal is simple: gentle, thoughtful care that helps dogs and cats move and feel better.</p>
    </div>
  </article>

  <article class="panel schedule">
    <div class="photo photo--cool" role="img" aria-label="Photo of a dog sitting"></div>
    <h2 class="band">Scheduling an appointment</h2>
    <div class="content">
      <p class="body-copy">Appointments are scheduled through your family veterinary clinic. Visits take place at the clinic, so your pet is seen in a familiar setting with records close at hand.</p>
      <p class="note">Please contact your veterinarian for information.</p>
    </div>
    <ul class="contact-list">
      <li><svg viewBox="0 0 10 10"><path d="M2 1l2 2-1 1.5c.7 1.3 1.2 1.8 2.5 2.5L7 6l2 2-1.5 1.5C4.5 9 1 5.5.5 2.5z" fill="#2c4f9e"/></svg>555-0142</li>
      <li><svg viewBox="0 0 10 10"><rect x=".5" y="2" width="9" height="6" fill="none" stroke="#2c4f9e"/><path d="M.5 2L5 5.5 9.5 2" fill="none" stroke="#2c4f9e"/></svg>willowcreekvet@postbloom.net</li>
      <li><svg viewBox="0 0 10 10"><circle cx="5" cy="5" r="4.3" fill="none" stroke="#2c4f9e"/><path d="M.7 5h8.6M5 .7c2 2.5 2 6.1 0 8.6M5 .7c-2 2.5-2 6.1 0 8.6" fill="none" stroke="#2c4f9e" stroke-width=".7"/></svg>willowcreekpetclinic.net</li>
      <li><svg viewBox="0 0 10 10"><rect x="1" y="1" width="8" height="8" fill="#2c4f9e"/></svg>Follow us online</li>
    </ul>
  </article>

  <article class="panel cover">
    <div class="brand-block">
      <div class="brand"><span class="brand__mark"></span><span class="brand__name">Willow Creek Pet Clinic</span></div>
      <p class="tagline">Gentle care at every step</p>
      <div class="rule"></div>
      <div class="rule rule--blue"></div>
    </div>
    <div class="photo photo--warm" role="img" aria-label="Photo of a small dog receiving care"></div>
    <p class="web">willowcreekpetclinic.net</p>
  </article>
</section>

<section class="sheet sheet--inside">
  <article class="panel overview">
    <div class="inside-top"></div>
    <div class="brand-block">
      <div class="brand"><span class="brand__mark"></span><span class="brand__name">Willow Creek Pet Clinic</span></div>
      <p class="tagline">Gentle care at every step</p>
    </div>
    <p class="body-copy">Acupuncture is a gentle therapy that uses fine needles at specific points to ease pain, reduce inflammation and support natural healing. Most pets relax during treatment, and many owners notice improved comfort and mobility within a few sessions. Treatments may be combined with laser therapy, massage and home exercises.</p>
    <div class="photo photo--bed" role="img" aria-label="Photo of a dog resting on a bed during treatment"></div>
  </article>

  <article class="panel conditions">
    <div class="inside-top"></div>
    <div class="photo photo--grass" role="img" aria-label="Photo of a dog running an agility course"></div>
    <h2 class="band">Conditions Commonly Treated with Acupuncture</h2>
    <ul class="cond-list">
      <li>Arthritis</li><li>Hip dysplasia</li><li>Back pain</li><li>Disc disease</li>
      <li>Nerve injury</li><li>Muscle strain</li><li>Allergies</li><li>Skin issues</li>
      <li>Digestive upset</li><li>Kidney support</li><li>Anxiety</li><li>Senior wellness</li>
      <li>Post-surgical recovery</li><li>Paralysis</li><li>Seizures</li><li>Urinary issues</li>
    </ul>
  </article>

  <article class="panel">
    <div class="inside-top"></div>
    <div class="therapy">
      <h2>Veterinary physical therapy and rehabilitation can help:</h2>
      <ul class="therapy-list">
        <li><b>Post-surgical recovery:</b> restores strength and range of motion.</li>
        <li><b>Arthritis:</b> eases stiffness and supports joint comfort.</li>
        <li><b>Weight loss:</b> low-impact exercise for healthy movement.</li>
        <li><b>Neurologic conditions:</b> rebuilds coordination and balance.</li>
        <li><b>Sport dogs:</b> conditioning and injury prevention.</li>
        <li><b>Senior pets:</b> keeps aging bodies active and comfortable.</li>
        <li>Therapies include laser, massage, stretching, balance work and home exercise plans tailored to your pet.</li>
      </ul>
    </div>
  </article>

  <div class="slogan-bar">Gentle care at every step</div>
</section>

</body>
</html>
```